Training company needs a Quick Reference Card design

We have draft skeleton of the design and most of the text. But we need a designer to take it the rest if the way.
I have designed a 2 page quick reference card - it is meant to be a 2-sided document. The first page is portrait, the back page can either be portrait or landscape, I'm not too concerned, whichever fits best.
Section called 'Maps' on front, a map is a collection of documents (like a manual), a topic is a document (like a page or section of a manual) and a block is a section of a document. The graphic is mean to illustrate the hierarchy but essentially a map is a big document with smaller documents in it.
Please use the company's logo colors to differentiate the different sections with minimal/ highlight only use of the darkest color, preferably.
Please use the icons for the corresponding Information types in the chart of the back - except please re-design the icons color scheme to match the company's logo/website colors.

Target Market(s)

Technical writers, after attending our training course, as an ongoing resource for them

Industry/Entity Type

It Company

Font styles to use
Sans Serif

Requirements
Must have
• Must adhere to look and feel of brand/ website. www.lumenrivet.com
Nice to have
• Please keep the design modern and slick looking, not too busy, easy to read

```html
<!DOCTYPE html>
<html lang="en">
<head>
<meta charset="utf-8">
<title>Quick Reference Card</title>
<link href="https://fonts.googleapis.com/css2?family=Montserrat:wght@600;700&family=Mulish:wght@300;400&display=swap" rel="stylesheet">
<style>
:root{
  --sky:#1ba0dc;
  --sky-bright:#14a6e0;
  --indigo:#2e3192;
  --ink:#1f1f2b;
  --body:#2b2b33;
  --white:#ffffff;
  --rule:#b9b9bd;
}
*{margin:0;padding:0;box-sizing:border-box}
html,body{width:970px;height:1200px;overflow:hidden;background:var(--white)}
.card{position:relative;width:970px;height:1200px;background:var(--white);font-family:'Mulish',sans-serif;color:var(--body)}
.abs{position:absolute}
.brand{left:64px;top:52px;display:flex;align-items:center;gap:12px}
.brand-dot{width:46px;height:46px;border-radius:50%;background:var(--indigo)}
.brand-name{font-family:'Montserrat',sans-serif;font-weight:700;font-size:26px;color:var(--indigo);letter-spacing:.3px}
.title-band{left:378px;top:30px;width:592px;height:82px;background:linear-gradient(90deg,var(--sky),var(--indigo));display:flex;align-items:center;padding-left:40px}
.title-band h1{font-family:'Montserrat',sans-serif;font-weight:700;font-size:35px;color:var(--white);letter-spacing:.5px}
.hero{left:68px;top:150px;width:840px;height:272px;border-radius:8px;background:linear-gradient(120deg,#e6f4fb 0%,#bfe3f5 45%,#c9cdea 100%)}
.pointer{width:1px;background:var(--sky)}
.pointer::before{content:"";position:absolute;top:-3px;left:-3px;width:7px;height:7px;border-radius:50%;background:var(--sky)}
.term h2{font-family:'Montserrat',sans-serif;font-weight:700;font-size:23px;color:var(--sky);line-height:1}
.term p{margin-top:6px;font-size:13.5px;line-height:19px;color:var(--body)}
.rules{left:0;top:560px;width:970px;height:264px;background:linear-gradient(100deg,var(--sky-bright) 0%,#2a6fc0 50%,var(--indigo) 100%)}
.rules h2{position:absolute;top:30px;width:100%;text-align:center;font-family:'Montserrat',sans-serif;font-weight:700;font-size:23px;color:var(--white);letter-spacing:.4px}
.rule{position:absolute;top:66px;width:290px;text-align:center;color:var(--white)}
.rule svg{display:block;margin:0 auto;width:66px;height:66px}
.rule h3{margin-top:18px;font-family:'Montserrat',sans-serif;font-weight:600;font-size:17px}
.rule p{margin-top:2px;font-weight:300;font-size:13.5px;line-height:19px;color:#e7f3fb}
.section-head{font-family:'Montserrat',sans-serif;font-weight:700;color:var(--sky);letter-spacing:.3px}
.questions{left:54px;top:864px;width:380px}
.questions .section-head{font-size:18px;line-height:20px}
.q-list{list-style:none;margin-top:22px}
.q-list li{display:flex;align-items:center;gap:10px;font-size:13.5px;height:33px}
.num{width:20px;height:20px;border-radius:50%;background:linear-gradient(135deg,var(--sky),var(--indigo));color:var(--white);font-family:'Montserrat',sans-serif;font-weight:700;font-size:11px;display:flex;align-items:center;justify-content:center}
.divider-h{left:36px;top:1028px;width:394px;height:1px;background:var(--rule)}
.divider-v{left:470px;top:845px;width:1px;height:309px;background:var(--rule)}
.arts{left:49px;top:1063px}
.arts .section-head{font-size:18px}
.art{position:absolute;top:1095px;display:flex;align-items:center;gap:8px;font-size:13.5px;line-height:18px}
.art-badge{width:54px;height:54px;border-radius:50%;background:radial-gradient(circle at 35% 30%,#3d7fd0,var(--indigo));color:var(--white);font-family:'Montserrat',sans-serif;font-weight:700;font-size:13px;display:flex;align-items:center;justify-content:center}
.principles-head{left:508px;top:866px;font-size:28px}
.principle{position:absolute;width:200px}
.principle h3{font-family:'Montserrat',sans-serif;font-weight:700;font-size:16px;color:var(--ink)}
.principle p{margin-top:10px;font-size:13.5px;line-height:19px}
.foot-band{left:0;top:1177px;width:970px;height:23px;background:linear-gradient(90deg,var(--sky),var(--indigo))}
</style>
</head>
<body>
<main class="card">
  <div class="abs brand"><span class="brand-dot"></span><span class="brand-name">Lumen Rivet</span></div>
  <div class="abs title-band"><h1>QUICK REFERENCE CARD</h1></div>

  <div class="abs hero" role="img" aria-label="Illustration of a blue folder holding documents, a document under a magnifying glass, and small scattered pages showing the map, topic and block hierarchy"></div>

  <span class="abs pointer" style="left:81px;top:355px;height:88px"></span>
  <span class="abs pointer" style="left:388px;top:313px;height:130px"></span>
  <span class="abs pointer" style="left:657px;top:250px;height:193px"></span>

  <section class="abs term" style="left:74px;top:446px;width:290px">
    <h2>A map</h2>
    <p>is a file that organizes topics into structured collections of information. Maps specify hierarchy and relationships among topics.</p>
  </section>
  <section class="abs term" style="left:383px;top:446px;width:250px">
    <h2>A topic</h2>
    <p>is a group of related blocks with a title. Use the chunking principle to group together relevant blocks.</p>
  </section>
  <section class="abs term" style="left:653px;top:446px;width:270px">
    <h2>A block</h2>
    <p>is a bite-sized chunk of information about one main idea that allows the writer to organize the material into logical sections.</p>
  </section>

  <section class="abs rules">
    <h2>GENERAL WRITING RULES</h2>
    <div class="rule" style="left:21px">
      <svg viewBox="0 0 66 66" fill="none" stroke="#fff" stroke-width="2.4">
        <circle cx="30" cy="36" r="26"/><circle cx="30" cy="36" r="18"/><circle cx="30" cy="36" r="10"/><circle cx="30" cy="36" r="3" fill="#fff"/>
        <path d="M30 36 L56 10"/><path d="M50 8 L56 10 L58 16"/><path d="M54 4 L58 10 L64 8"/>
      </svg>
      <h3>Effective sentences</h3>
      <p>One main agent, action &amp; outcome. Use active voice and simplest tense possible. No more than 7 sentences per paragraph. Use lists and tables.</p>
    </div>
    <div class="rule" style="left:340px">
      <svg viewBox="0 0 66 66" fill="none" stroke="#fff" stroke-width="2">
        <rect x="6" y="6" width="54" height="54" stroke-dasharray="2 3"/>
        <path d="M20 18 H46 V26 M20 18 V26 M33 18 V50 M26 50 H40" stroke-width="2.6"/>
      </svg>
      <h3>Special characters</h3>
      <p>Avoid special characters, spell out words instead. Remove parentheses, colons and dashes. Avoid using quotation marks and slashes.</p>
    </div>
    <div class="rule" style="left:651px">
      <svg viewBox="0 0 66 66" fill="none" stroke="#fff" stroke-width="2.4">
        <rect x="12" y="6" width="48" height="54" rx="3"/><path d="M12 16 H6 V56 A4 4 0 0 0 14 56"/>
        <rect x="18" y="14" width="14" height="12"/><path d="M36 15 H54 M36 21 H54 M36 27 H54 M18 33 H54 M18 39 H54 M18 45 H54 M18 51 H54"/>
      </svg>
      <h3>Plain language</h3>
      <p>Write in short sentences. Provide useful titles. Use clear familiar words. Avoid excess words. Be consistent.</p>
    </div>
  </section>

  <section class="abs questions">
    <h2 class="section-head">3 QUESTIONS TO ASK BEFORE<br>YOU START WRITING:</h2>
    <ol class="q-list">
      <li><span class="num">1</span>What is the purpose of this information?</li>
      <li><span class="num">2</span>What is the desired user response of this information?</li>
      <li><span class="num">3</span>Who is the audience?</li>
    </ol>
  </section>

  <span class="abs divider-h"></span>

  <h2 class="abs arts section-head">2 TYPES OF LANGUAGE ARTS:</h2>
  <div class="art" style="left:47px"><span class="art-badge">LAFI</span><span>Language Arts<br>For Information</span></div>
  <div class="art" style="left:249px"><span class="art-badge">LAFPR</span><span>Language Arts For<br>Personal Response</span></div>

  <span class="abs divider-v"></span>

  <h2 class="abs section-head principles-head">4 COGNITIVE PRINCIPLES</h2>
  <div class="principle" style="left:508px;top:908px"><h3>1. Consistency</h3><p>Use similar terms and structures. Pick a term and stick with it. Use the same sequence of blocks. Use consistent styles.</p></div>
  <div class="principle" style="left:743px;top:908px"><h3>2. Chunking</h3><p>Maximum of nine (7 +/- 2) items in a list, rows in a table, blocks in a topic, or topics in a map.</p></div>
  <div class="principle" style="left:508px;top:1043px"><h3>3. Relevance</h3><p>Group similar items together. Separate relevance? Separate block. Irrelevant? Delete it.</p></div>
  <div class="principle" style="left:743px;top:1043px"><h3>4. Titling</h3><p>Name everything. Name every block, every topic, every map and every table column.</p></div>

  <div class="abs foot-band"></div>
</main>
</body>
</html>
```